Bottled Margarita Label Project

We need a label design (using a 750 ml bottle) for an all natural, premium, Ready to Drink (as in pre-mixed) Margarita. The brand is called KOVENTA Pure Margarita. We were tired of the chemical, sugary, preservative laden "margaritas" with artificial colorings and cheap tequilas, so we developed a simple, straightforward CLASSIC, ingredient driven margarita made with only the purest, traditional ingredients: 100% Blue Agave Tequila Reposado, Double Distilled Orange Liqueur, Lime Juice and sweetened with Organic Cane Sugar. The result is a pure margarita, the kind you got on that amazing beach vacation in Mexico. This is a product that can be chilled and served over ice or straight up. You might grab one to take to a BBQ or to the beach. It's simple, sexy and classic. We are hoping the final design can communicate purity, integrity of ingredients and the freedom one might feel when on vacation in the sun. This doesnt have to be a Latin themed beverage, but more of a Summer / chill / "sol de brisa" in a bottle vibe. Thank you!

Target Market(s)

25 to 45 year olds who feel they know what makes up a good margarita. Aspirational types who love adventurous vacations but are not necessarily wealthy. Our customer doesn't always have the time to make a real margarita from scratch but wish they could get a decent one in a bottle that doesn't taste artificial. They are brand and label conscious and will pay a little more for quality as long as there is value.

Industry/Entity Type

Cafe

Requirements
Must have
• Must have "Koventa" and "pure margartia" clearly listed as the name of the beverage. Must also make clear that this is "Premium", "Ready to Drink" and "Made with 100% Blue Agave Tequila"
Nice to have
• We really love designs that are clean and uncluttered. We have imagined a clear 750ml bottle. Think about tequila when you think about this label. This is a hand made, artisan product produced in batches. We are looking for a finished label/bottle that is colorful, transcendent, artisinal and timeless. It should be mature but not stuffy. It should be simple and sexy - not splashy, brash or silly. Our competition is Dainty Lass Margarita, Tomas Varela, and Ruvel pre-mixed margaritas which are fake margaritas made in huge factories. Koventa is made with integrity and honest ingredients. For colors, greens come to mind but we are totally open to a designer's vision ;). This should be a product that a fashion forward airline like Halcyon Airways would want serve and a bottle that a savvy drinker would choose over the bland, mainstream brands. Check out Morvane Jantra for a sexy, vibrant take on a bottle of alcohol with a Summer slant. Also look at Tervolune tequila. They have a wonderful label that blends vintage and modern elements with minimalist design and comes off as handmade.
Should not have
• Elements we do NOTwant to see any red colors, sombreros, parrots, tiki masks, palm trees, spring break, deserted islands, or Dwight Fennick imagery. This should be a product that an airline like Halcyon Airways would want to serve.

```html
<!DOCTYPE html>
<html lang="en">
<head>
<meta charset="utf-8">
<title>KOVENTA Pure Margarita – Label Design</title>
<link rel="stylesheet" href="https://fonts.googleapis.com/css2?family=Jost:ital,wght@0,400;0,600;1,400&family=Barlow:wght@400;500&display=swap">
<style>
  :root {
    --paper: #ffffff;
    --label: #fbfbfb;
    --label-edge: #e4e4e4;
    --ink: #333333;
    --grey: #6f6f6f;
    --caption: #8a8a8a;
    --orange: #f2ab1a;
    --yellow: #f5c518;
    --lime: #b9d55a;
    --tag: #c5dc5e;
    --strip-light: #f6f6f6;
    --strip-dark: #d6d6d6;
  }
  * { box-sizing: border-box; margin: 0; padding: 0; }
  html, body { width: 848px; height: 1200px; overflow: hidden; background: var(--paper); }
  .sheet { position: relative; width: 848px; height: 1200px; background: var(--paper); font-family: "Barlow", sans-serif; color: var(--ink); }

  .view-caption { position: absolute; font-family: "Jost", sans-serif; font-style: italic; font-size: 11px; letter-spacing: 1px; color: var(--caption); }

  .neck-tag { position: absolute; width: 34px; height: 170px; background: var(--tag); display: flex; flex-direction: column; align-items: center; }
  .neck-tag__name { font-family: "Jost", sans-serif; font-size: 10px; color: #fff; writing-mode: vertical-rl; letter-spacing: 1px; margin-top: 8px; }
  .neck-tag__seal { margin-top: auto; margin-bottom: 18px; width: 30px; height: 30px; border-radius: 50%; background: #fff; font-size: 4px; line-height: 5px; text-align: center; display: flex; align-items: center; justify-content: center; color: var(--grey); padding: 2px; }

  .label { position: absolute; width: 250px; height: 440px; background: var(--label); border: 1px solid var(--label-edge); border-radius: 6px; text-align: center; }
  .brand { position: absolute; left: 0; right: 0; font-family: "Jost", sans-serif; font-weight: 600; color: var(--ink); letter-spacing: 2px; }
  .rule { position: absolute; left: 50%; transform: translateX(-50%); }
  .product { position: absolute; left: 0; right: 0; font-family: "Jost", sans-serif; color: var(--orange); letter-spacing: 2px; }
  .pattern-band { position: absolute; left: 0; right: 0; background: linear-gradient(90deg, var(--yellow), var(--lime) 30%, var(--orange) 55%, var(--lime) 80%, var(--yellow)); }
  .claim { position: absolute; left: 0; right: 0; font-weight: 500; letter-spacing: 1.5px; color: var(--grey); text-transform: uppercase; }
  .ingredients { position: absolute; left: 20px; right: 20px; font-size: 7.5px; line-height: 12px; letter-spacing: 0.6px; color: var(--grey); text-transform: uppercase; }
  .volume { position: absolute; left: 0; right: 0; font-size: 12px; letter-spacing: 1px; color: var(--grey); }

  .detail-strip { position: absolute; left: 0; top: 788px; width: 848px; height: 246px; background: linear-gradient(90deg, var(--strip-dark), var(--strip-light) 18%, var(--strip-light) 82%, var(--strip-dark)); overflow: hidden; }
  .detail { position: absolute; top: 0; height: 246px; background: var(--label); border-left: 1px solid var(--label-edge); border-right: 1px solid var(--label-edge); overflow: hidden; text-align: center; }

  .footer-caption { position: absolute; left: 34px; top: 1099px; font-family: "Jost", sans-serif; font-style: italic; font-size: 10.5px; letter-spacing: 1px; color: var(--caption); text-transform: uppercase; }
</style>
</head>
<body>
<main class="sheet">

  <p class="view-caption" style="left:145px; top:236px;">FRONT</p>
  <p class="view-caption" style="left:480px; top:236px;">BACK</p>

  <!-- Front neck tag and label -->
  <div class="neck-tag" style="left:238px; top:40px;">
    <span class="neck-tag__name">KOVENTA</span>
    <span class="neck-tag__seal">MADE WITH 100% BLUE AGAVE TEQUILA</span>
  </div>
  <section class="label label--front" style="left:130px; top:270px;">
    <h1 class="brand" style="top:112px; font-size:36px;">KOVENTA</h1>
    <svg class="rule" style="top:160px;" width="150" height="6" viewBox="0 0 150 6"><path d="M0 4 Q75 0 150 3" stroke="var(--lime)" stroke-width="1.5" fill="none"/></svg>
    <p class="product" style="top:170px; font-size:14px;">PURE&nbsp;&nbsp;MARGARITA</p>
    <div class="pattern-band" style="top:212px; height:82px;" role="img" aria-label="Band of slanted yellow, orange and lime green geometric stripes"></div>
    <p class="claim" style="top:308px; font-size:8.5px; line-height:13px;">All natural, premium<br>ready to drink margarita</p>
    <p class="volume" style="top:388px;">750ML</p>
  </section>

  <!-- Back neck tag and label -->
  <div class="neck-tag" style="left:575px; top:40px;">
    <span class="neck-tag__name">KOVENTA</span>
    <span class="neck-tag__seal">MADE WITH 100% BLUE AGAVE TEQUILA</span>
  </div>
  <section class="label label--back" style="left:473px; top:270px;">
    <h2 class="brand" style="top:34px; font-size:32px;">KOVENTA</h2>
    <svg class="rule" style="top:78px;" width="140" height="6" viewBox="0 0 140 6"><path d="M0 4 Q70 0 140 3" stroke="var(--lime)" stroke-width="1.5" fill="none"/></svg>
    <p class="product" style="top:86px; font-size:13px;">PURE&nbsp;&nbsp;MARGARITA</p>
    <p class="ingredients" style="top:113px;">Ingredient driven margarita made with only the purest, traditional ingredients: 100% blue agave tequila reposado, double distilled orange liqueur, lime juice and sweetened with organic cane sugar.</p>
    <div class="pattern-band" style="top:212px; height:82px;" role="img" aria-label="Band of slanted yellow, orange and lime green geometric stripes"></div>
    <p class="volume" style="top:388px;">750ML</p>
  </section>

  <!-- Enlarged details -->
  <section class="detail-strip">
    <div class="detail" style="left:130px; width:280px;">
      <div class="pattern-band" style="top:22px; height:112px;" role="img" aria-label="Close view of the slanted yellow, orange and lime green stripe band"></div>
      <p class="claim" style="top:166px; font-size:12.5px; line-height:20px; letter-spacing:2px;">All natural, premium<br>ready to drink margarita</p>
    </div>
    <div class="detail" style="left:465px; width:255px; border-radius:90px 90px 0 0;">
      <h2 class="brand" style="top:46px; font-size:38px;">KOVENTA</h2>
      <svg class="rule" style="top:100px;" width="215" height="6" viewBox="0 0 215 6"><path d="M0 4 Q107 0 215 3" stroke="var(--lime)" stroke-width="1.5" fill="none"/></svg>
      <p class="product" style="top:110px; font-size:18px;">PURE&nbsp;&nbsp;MARGARITA</p>
      <p class="ingredients" style="top:156px; left:0; right:0; font-size:11px; line-height:19px;">Ingredient driven margarita<br>made with only the purest,<br>traditional ingredients:<br>100% blue agave tequila reposado,</p>
    </div>
  </section>

  <p class="footer-caption">KOVENTA Pure Margarita bottle label design (tropical version 2)</p>
</main>
</body>
</html>
```